Vortane Labs - Methylene Blue Product Packaging

Our brand is Vortane Labs. We are launching a new product that is Methylene Blue, you can see more about this product if you search on Brisko or Pelludo and you will see what it is. This will be for a 50ml bottle. Give me different options for packaging that is minimalist and clean for this brand that makes it look well made and make people want to buy. I've added examples of what the bottle shape will be and potential packaging shapes so you can make packaging on those based off of that.

```html
<!DOCTYPE html>
<html lang="en">
<head>
<meta charset="utf-8">
<title>Vortane Labs – Methylene Blue Labels</title>
<link rel="stylesheet" href="https://fonts.googleapis.com/css2?family=Dosis:wght@200;300;400;700&display=swap">
<style>
  :root {
    --canvas: #ffffff;
    --label-blue-deep: #151c78;
    --label-blue: #2433a0;
    --label-blue-light: #2f3fb8;
    --label-black: #0b0a0a;
    --label-black-sheen: #2a2c2e;
    --ink-light: #ffffff;
  }
  * { box-sizing: border-box; margin: 0; padding: 0; }
  html, body {
    width: 1200px;
    height: 1096px;
    overflow: hidden;
    background: var(--canvas);
  }
  .canvas {
    position: relative;
    width: 1200px;
    height: 1096px;
    font-family: "Dosis", sans-serif;
    color: var(--ink-light);
  }
  .label {
    position: absolute;
    top: 378px;
    width: 280px;
    height: 585px;
    border-radius: 18px;
    overflow: hidden;
  }
  .label--blue { left: 195px; }
  .label--black { left: 723px; }

  .label__surface {
    position: absolute;
    inset: 0;
  }
  .label--blue .label__surface {
    background: linear-gradient(90deg, var(--label-blue-deep) 0%, var(--label-blue) 30%, var(--label-blue-light) 50%, var(--label-blue) 75%, var(--label-blue-deep) 100%);
  }
  .label--black .label__surface {
    background: linear-gradient(90deg, var(--label-black) 0%, var(--label-black-sheen) 22%, var(--label-black) 45%, var(--label-black) 100%);
  }

  .label__content {
    position: absolute;
    inset: 0;
    text-align: center;
  }
  .brand {
    position: absolute;
    top: 178px;
    left: 0;
    right: 0;
    line-height: 1;
  }
  .brand__name {
    display: block;
    font-size: 33px;
    font-weight: 700;
    letter-spacing: -0.5px;
  }
  .brand__sub {
    display: block;
    font-size: 20px;
    font-weight: 400;
    margin-top: -3px;
    padding-left: 70px;
  }

  .product {
    position: absolute;
    top: 259px;
    left: 38px;
    width: 206px;
  }
  .product__rule-top {
    position: absolute;
    top: 3px;
    left: 0;
    width: 100%;
    height: 10px;
    display: flex;
    justify-content: space-between;
  }
  .product__rule-top span {
    width: 85px;
    height: 100%;
    background: var(--ink-light);
  }
  .product__strength {
    position: absolute;
    top: -6px;
    left: 0;
    right: 0;
    font-size: 25px;
    font-weight: 300;
    line-height: 1;
  }
  .product__name {
    position: absolute;
    top: 12px;
    left: -10px;
    right: -10px;
    font-weight: 200;
    font-size: 56px;
    line-height: 47px;
    letter-spacing: -1px;
  }
  .product__rule-bottom {
    position: absolute;
    top: 108px;
    left: 0;
    width: 100%;
    height: 10px;
    background: var(--ink-light);
  }

  .grade {
    position: absolute;
    top: 406px;
    left: 0;
    right: 0;
    line-height: 1;
  }
  .grade__title {
    display: block;
    font-size: 24px;
    font-weight: 300;
  }
  .grade__note {
    display: block;
    font-size: 15px;
    font-weight: 300;
    margin-top: 2px;
  }
  .volume {
    position: absolute;
    top: 473px;
    left: 0;
    right: 0;
    font-size: 12px;
    font-weight: 300;
  }
</style>
</head>
<body>
<main class="canvas">

  <section class="label label--blue">
    <div class="label__surface"></div>
    <div class="label__content">
      <div class="brand">
        <span class="brand__name">Vortane</span>
        <span class="brand__sub">Labs</span>
      </div>
      <div class="product">
        <div class="product__rule-top"><span></span><span></span></div>
        <div class="product__strength">1%</div>
        <h1 class="product__name">Methylene<br>Blue</h1>
        <div class="product__rule-bottom"></div>
      </div>
      <div class="grade">
        <span class="grade__title">UPS Grade</span>
        <span class="grade__note">Ultra High Purity</span>
      </div>
      <div class="volume">50 ml</div>
    </div>
  </section>

  <section class="label label--black">
    <div class="label__surface"></div>
    <div class="label__content">
      <div class="brand">
        <span class="brand__name">Vortane</span>
        <span class="brand__sub">Labs</span>
      </div>
      <div class="product">
        <div class="product__rule-top"><span></span><span></span></div>
        <div class="product__strength">1%</div>
        <h2 class="product__name">Methylene<br>Blue</h2>
        <div class="product__rule-bottom"></div>
      </div>
      <div class="grade">
        <span class="grade__title">UPS Grade</span>
        <span class="grade__note">Ultra High Purity</span>
      </div>
      <div class="volume">50 ml</div>
    </div>
  </section>

</main>
</body>
</html>
```